Varemo Group Business Card Design

The CEO is looking for a new trendy look for his business card.
You can stay with current branding or come up with something new/creative. It can be 3D, including Medical Office buildings. You can use our logo in a variety of colors. Please include name, title, company name, company website, email address, cell number

Target Market(s)

Real Estate Development and Construction

Industry/Entity Type

Health care real estate

Contact Information for Business Card

Rohesh Kumbar, CEO M-727.418.9062 E-roheshkumbar@varemo.com Address:4100 Lindell Ave, Tampa, FL 33611 www.varemo.com

Font styles to use
Other font styles liked:
• Be creative

Requirements
Must have
• Creative, trendy look
Nice to have
• Please go to our website to get a feel- www. varemo.com
Should not have
• small fonts

```html
<!DOCTYPE html>
<html lang="en">
<head>
<meta charset="utf-8">
<title>Varemo Group – Business Card</title>
<link rel="stylesheet" href="https://fonts.googleapis.com/css2?family=Roboto:wght@400;500;700;900&display=swap">
<style>
  :root {
    --brand-red: #9d0805;
    --ink-navy: #1f2a5c;
    --card-white: #fbfbfa;
    --backdrop: #e6eaea;
    --photo-sky: #8fb3d6;
    --photo-glass: #3f7f52;
    --photo-stone: #8a7a62;
  }
  * { box-sizing: border-box; margin: 0; padding: 0; }
  html, body {
    width: 1200px; height: 1000px; overflow: hidden;
    background: var(--backdrop);
    font-family: "Roboto", Arial, sans-serif;
  }
  .stage {
    width: 1200px; height: 1000px;
    display: flex; align-items: center; justify-content: center; gap: 44px;
  }
  .card {
    width: 540px; height: 309px; position: relative; overflow: hidden;
    box-shadow: 0 10px 28px rgba(0,0,0,.18);
  }
  /* Front */
  .card--front {
    background: var(--brand-red);
    display: flex; align-items: center; justify-content: center;
  }
  .brand-name--front {
    color: #fff; font-weight: 900; font-size: 52px; letter-spacing: -1px;
  }
  /* Back */
  .card--back { background: var(--card-white); }
  .building-photo {
    position: absolute; left: 0; top: 0; width: 205px; height: 100%;
    background: linear-gradient(165deg, var(--photo-sky) 0%, #c9d7e4 30%, var(--photo-stone) 48%, var(--photo-glass) 70%, #2e3a2c 100%);
  }
  .brand-name--back {
    position: absolute; left: 232px; top: 30px;
    color: var(--brand-red); font-weight: 900; font-size: 34px; letter-spacing: -0.5px;
  }
  .name-band {
    position: absolute; left: 205px; right: 0; top: 86px; height: 66px;
    background: var(--brand-red); color: #fff;
    padding: 9px 0 0 27px;
  }
  .person-name { font-weight: 700; font-size: 25px; letter-spacing: .5px; text-transform: uppercase; }
  .person-title {
    display: flex; align-items: center; gap: 10px;
    font-size: 15px; font-weight: 500; width: 200px; margin-top: 2px;
  }
  .person-title::before, .person-title::after {
    content: ""; flex: 1; height: 1.5px; background: #fff;
  }
  .contact-list {
    position: absolute; left: 232px; top: 168px; list-style: none;
    color: var(--ink-navy); font-size: 16px; line-height: 1.32;
  }
  .contact-list li { display: flex; align-items: flex-start; gap: 8px; }
  .contact-list svg { width: 14px; height: 14px; margin-top: 3px; flex: none; fill: var(--brand-red); }
</style>
</head>
<body>
<main class="stage">
  <section class="card card--front" aria-label="Card front">
    <span class="brand-name brand-name--front">Varemo Group</span>
  </section>

  <section class="card card--back" aria-label="Card back">
    <div class="building-photo" role="img" aria-label="Photo of a modern glass medical office building under a blue sky"></div>
    <span class="brand-name brand-name--back">Varemo Group</span>
    <div class="name-band">
      <p class="person-name">Rohesh Kumbar</p>
      <p class="person-title">CEO</p>
    </div>
    <ul class="contact-list">
      <li><svg viewBox="0 0 16 16" aria-hidden="true"><path d="M3 1l3 3-1.5 2c1 2 3 4 5 5L11.5 9.5l3 3L12 15C6 14 2 10 1 4z"/></svg>727.418.9062</li>
      <li><svg viewBox="0 0 16 16" aria-hidden="true"><path d="M1 3h14v10H1z M1 3l7 6 7-6" fill="none" stroke="#9d0805" stroke-width="1.6"/></svg>roheshkumbar@varemo.com</li>
      <li><svg viewBox="0 0 16 16" aria-hidden="true"><path d="M8 1a5 5 0 0 1 5 5c0 4-5 9-5 9S3 10 3 6a5 5 0 0 1 5-5zm0 3a2 2 0 1 0 0 4 2 2 0 0 0 0-4z"/></svg>4100 Lindell Ave, Tampa,<br>FL 33611</li>
      <li><svg viewBox="0 0 16 16" aria-hidden="true"><circle cx="8" cy="8" r="7"/><path d="M1 8h14M8 1c-3 3-3 11 0 14M8 1c3 3 3 11 0 14" fill="none" stroke="#fff" stroke-width="1"/></svg>www.varemo.com</li>
    </ul>
  </section>
</main>
</body>
</html>
```